3 Politically Incorrect Greeting Cards

I would like to see some clean, colorful, and modern designs for 3 "politically incorrect" greeting cards aimed at young, single, successful women. I would like them to say:

Card 1: " Congratulations on not marrying the wrong person"
Card 2: " Congratulations on buying a house without a husband"
Card 3: " Thank you for not forgetting about me now that you have a boyfriend"

My initial thought was to have a white background with simple black writing, but I think a colorful background with a white text box in the middle might be more appropriate. I can't imagine the cards having any images/icons on them, but I'm open to suggestions if you think it would improve on the design. You guys are likely more creative than I am.

I've included a couple pics of looks I like - but like I said - I'm open to suggestions and what I like may not be appropriate for these cards. All the cards can have a similar esthetic or theme (maybe the same fonts but different colors or different color florals in each) or they can be completely different.

Target Market(s)

Young, single, successful women mid-20s to mid 40's.

Font styles to use
Serif
Sans Serif
Other font styles liked:
• Watercolour lettering maybe

Colors

Designer to choose colors to be used in the design.

Requirements
Must have
• Clean, colorful, bright, professional looking. The right tone for the message.
• I think the message is bold so the writing and colors have to be as well. I have included examples of ideas I like.
Nice to have
• Images, illustrations, icons, maybe patterns or some decorative details. Something to make the card more interesting than just the words (like the blue background with black letters one I made). I like a bright pattern with a white box in the center with the text.
Should not have
• Special effects, galaxy pictures, ugly images, bland colors.

```html
<!DOCTYPE html>
<html lang="en">
<head>
<meta charset="utf-8">
<title>Greeting Card Set</title>
<link href="https://fonts.googleapis.com/css2?family=Great+Vibes&family=Oswald:wght@300;400&display=swap" rel="stylesheet">
<style>
  :root {
    --page: #ffffff;
    --sky: #c8e7f7;
    --lavender: #e2dde9;
    --mist: #e8e9f1;
    --label: #6b8ec4;
    --ink: #ffffff;
  }
  html, body {
    margin: 0;
    padding: 0;
    width: 1200px;
    height: 1200px;
    overflow: hidden;
    background: var(--page);
  }
  .card-strip {
    position: absolute;
    left: 362px;
    top: 51px;
    width: 500px;
    height: 1090px;
    display: flex;
    flex-direction: column;
  }
  .card {
    position: relative;
    flex: 1 1 0;
  }
  .card--sky { background: var(--sky); }
  .card--lavender { background: var(--lavender); }
  .card--mist { background: var(--mist); }

  .label {
    position: absolute;
    left: 103px;
    width: 294px;
    height: 67px;
  }
  .card--sky .label { top: 164px; }
  .card--lavender .label { top: 149px; }
  .card--mist .label { top: 150px; }

  .label-shape {
    position: absolute;
    inset: 0;
    width: 294px;
    height: 67px;
  }
  .label-shape path { fill: var(--label); }

  .label-text {
    position: absolute;
    inset: 0;
    display: flex;
    flex-direction: column;
    align-items: center;
    justify-content: center;
    color: var(--ink);
    text-align: center;
  }
  .headline {
    font-family: "Great Vibes", cursive;
    font-size: 25px;
    line-height: 24px;
    height: 24px;
  }
  .message {
    font-family: "Oswald", sans-serif;
    font-weight: 300;
    font-size: 9.5px;
    line-height: 11px;
    text-transform: uppercase;
    letter-spacing: 0.1px;
    max-width: 160px;
    margin-top: 8px;
  }
  .message--wide { max-width: 200px; }
</style>
</head>
<body>
  <main class="card-strip">
    <section class="card card--sky">
      <div class="label">
        <svg class="label-shape" viewBox="0 0 294 67" aria-hidden="true">
          <path d="M0,33 C20,30 30,20 30,8 Q30,0 42,0 H252 Q264,0 264,8 C264,20 274,30 294,33 C274,36 264,46 264,59 Q264,67 252,67 H42 Q30,67 30,59 C30,46 20,36 0,33 Z"/>
        </svg>
        <div class="label-text">
          <div class="headline">Thank you</div>
          <div class="message">For not forgetting about me now that you have a boyfriend</div>
        </div>
      </div>
    </section>

    <section class="card card--lavender">
      <div class="label">
        <svg class="label-shape" viewBox="0 0 294 67" aria-hidden="true">
          <path d="M0,33 C20,30 30,20 30,8 Q30,0 42,0 H252 Q264,0 264,8 C264,20 274,30 294,33 C274,36 264,46 264,59 Q264,67 252,67 H42 Q30,67 30,59 C30,46 20,36 0,33 Z"/>
        </svg>
        <div class="label-text">
          <div class="headline">Congratulations</div>
          <div class="message message--wide">On not marrying the wrong person</div>
        </div>
      </div>
    </section>

    <section class="card card--mist">
      <div class="label">
        <svg class="label-shape" viewBox="0 0 294 67" aria-hidden="true">
          <path d="M0,33 C20,30 30,20 30,8 Q30,0 42,0 H252 Q264,0 264,8 C264,20 274,30 294,33 C274,36 264,46 264,59 Q264,67 252,67 H42 Q30,67 30,59 C30,46 20,36 0,33 Z"/>
        </svg>
        <div class="label-text">
          <div class="headline">Congratulations</div>
          <div class="message message--wide">On buying a house without a husband</div>
        </div>
      </div>
    </section>
  </main>
</body>
</html>
```